Rallyvo.net is a multi-sport platform that connects players, clubs, coaches, and organizers in one ecosystem.

Core value:
- Players can instantly find or create games across sports (padel, pickleball, tennis, soccer, etc.)
- Clubs can manage players, classes, staff, and tournaments in one place
- Coaches and organizers can create events and earn money directly through the platform

Key differentiator:
Rallyvo is not just for finding games — it is a revenue engine for clubs and sports communities.

Main features to highlight:
- Find and join games instantly
- Create games without coordination friction
- Club management (players, classes, payments)
- Coaches offering lessons and programs
- Tournaments and events between clubs
- Fill empty court time with automated or quick-created events

Business model:
- Free to join
- Platform takes a small fee on transactions (events, classes, subscriptions)

Tagline:
“Let the Games Begin & Pick Your Challenge”

Tone:
Modern, premium, community-driven, and action-oriented.
Focus on simplicity, energy, and real usage scenarios.

Target Market(s)

multi-sport platform that connects players, clubs, coaches, and organizers in one ecosystem.

Industry/Entity Type

Sport

Coding

Coded - Design and coding required

Number of Pages Required

3 page

Requirements
Must have
• Build you the exact Webflow structure (class-by-class export)
Nice to have
• Html y css

```html
<!DOCTYPE html>
<html lang="en">
<head>
<meta charset="utf-8">
<title>Rallyvo – Play More. Connect Faster.</title>
<link href="https://fonts.googleapis.com/css2?family=Lexend:wght@300;400;500;600;700&display=swap" rel="stylesheet">
<style>
:root{
  --bg:#0a0b0a;
  --green:#8cc63f;
  --green-bright:#a4e03a;
  --green-deep:#0f6b3a;
  --lime:#b5e61d;
  --white:#ffffff;
  --muted:#c9cfc5;
  --line:#2a2d29;
  --cta-text:#27421a;
}
*{box-sizing:border-box;margin:0;padding:0}
html,body{width:1200px;height:3788px;overflow:hidden;background:var(--bg);color:var(--white);font-family:"Lexend",sans-serif}
a{color:inherit;text-decoration:none}
.page{position:relative;width:1200px;height:3788px}
.section{position:absolute;left:0;width:1200px;overflow:hidden}
.brand{display:flex;align-items:center;gap:12px;font-weight:500;font-size:34px;color:var(--white)}
.brand-dot{width:62px;height:62px;border-radius:50%;background:var(--green)}
.btn{display:inline-flex;align-items:center;justify-content:center;border-radius:30px;font-weight:600;font-size:16px}
.btn-lime{background:var(--lime);color:#0b1a05}
.btn-deep{background:var(--green-deep);color:var(--white)}
.accent{color:var(--green-bright)}

/* nav + hero */
.hero{top:0;height:700px;background:radial-gradient(ellipse 420px 300px at 920px 500px,rgba(140,220,40,.75),transparent 70%),radial-gradient(ellipse 300px 200px at 1150px 120px,rgba(140,220,40,.4),transparent 70%),var(--bg);border-bottom:1px solid var(--line)}
.nav{position:absolute;top:18px;left:111px;right:112px;height:66px;display:flex;align-items:center;justify-content:space-between}
.nav-links{display:flex;align-items:center;font-size:15px;color:var(--muted);margin-left:180px}
.nav-links a{padding:0 30px}
.nav-links .active{color:var(--green-bright);font-weight:500}
.login{background:var(--white);color:#111;border-radius:22px;height:38px;padding:0 14px 0 18px;font-size:15px;font-weight:500;display:flex;align-items:center;gap:10px}
.login i{width:20px;height:20px;border-radius:50%;background:#111;display:block}
.nav-rule{position:absolute;top:105px;left:0;right:0;height:1px;background:var(--line)}
.hero-copy{position:absolute;left:109px;top:204px}
.hero-label{font-size:30px;font-weight:500;margin-bottom:10px}
.hero-title{font-size:58px;font-weight:500;line-height:62px;letter-spacing:.5px}
.hero-text{margin-top:22px;font-size:16px;line-height:30px;width:560px}
.hero-actions{margin-top:28px;display:flex;gap:22px}
.hero-actions .btn-lime{width:141px;height:45px}
.hero-actions .btn-deep{width:172px;height:45px}
.app-preview{position:absolute;left:735px;top:125px;width:340px;height:505px;border-radius:44px;background:linear-gradient(160deg,#1d211c,#0c0e0b 60%,#3a6d14);border:3px solid #3c4238;transform:rotate(-4deg)}

/* stats */
.stats{top:700px;height:230px;display:flex;padding:0 112px;border-bottom:1px solid var(--line)}
.stat{flex:1;text-align:center;padding-top:12px;border-right:1px solid var(--line);margin:34px 0}
.stat:last-child{border-right:none}
.stat svg{width:46px;height:46px;stroke:var(--white);fill:none;stroke-width:2}
.stat-num{font-size:48px;font-weight:600;color:var(--green-bright);margin-top:8px;line-height:56px}
.stat-label{font-size:16px;margin-top:6px}

/* audiences */
.audiences{top:930px;height:710px;background:radial-gradient(ellipse 240px 220px at 40px 80px,rgba(140,220,40,.85),transparent 70%),var(--bg);text-align:center}
.sec-title{font-size:38px;font-weight:500;line-height:48px}
.audiences .sec-title{margin-top:92px}
.sec-sub{font-size:16px;color:var(--muted);margin-top:20px}
.cards{position:absolute;top:270px;left:111px;display:flex;gap:30px}
.card{width:306px;height:350px;border-radius:26px;border:1px solid #3d4a30;background:linear-gradient(180deg,#121412 0%,#111 55%,#2f6a10 100%);text-align:left;padding:28px 24px}
.card-icon{width:80px;height:80px;border-radius:50%;background:#0e0f0e;border:2px solid var(--green);display:flex;align-items:center;justify-content:center}
.card-icon svg{width:40px;height:40px;stroke:var(--white);fill:none;stroke-width:2}
.card h3{font-size:17px;font-weight:600;margin-top:24px;letter-spacing:.5px}
.card p{font-size:12.5px;line-height:23px;color:var(--muted);margin-top:12px}
.card ul{list-style:none;margin-top:14px}
.card li{font-size:13px;line-height:25px;display:flex;align-items:center;gap:8px}
.card li svg{width:14px;height:14px;stroke:var(--green-bright);fill:none;stroke-width:3}

/* about */
.about{top:1640px;height:675px;background:radial-gradient(ellipse 520px 220px at 300px 0px,rgba(140,220,40,.55),transparent 70%),radial-gradient(ellipse 300px 160px at 100px 560px,rgba(110,190,30,.6),transparent 70%),var(--bg);border-bottom:1px solid var(--line)}
.about-media{position:absolute;left:111px;top:113px;width:412px;height:412px;border-radius:50%;border:3px solid var(--green);background:radial-gradient(circle at 65% 65%,#dfe6ea 0 12%,#1d3550 26%,#0c1b2c 60%,#b45a1a 100%)}
.about-copy{position:absolute;left:600px;top:95px;width:488px}
.about-copy h2{font-size:38px;font-weight:500}
.about-copy p{font-size:14.5px;line-height:26px;text-align:justify;margin-top:22px}
.about-copy .btn{margin-top:26px;width:142px;height:44px;background:var(--green);color:#0b1a05}

/* cities */
.cities{top:2315px;height:675px;text-align:center;background:var(--bg)}
.cities .sec-title{margin-top:80px}
.cities .sec-sub{margin-top:18px}
.city-box{position:absolute;left:210px;top:215px;width:780px;height:358px;border-radius:30px;border:1px solid #4d7a20;background:radial-gradient(ellipse 400px 220px at 80% 110%,rgba(140,220,40,.9),transparent 70%),radial-gradient(ellipse 220px 140px at 0% 0%,rgba(140,220,40,.5),transparent 70%),#0d0e0d}
.globe{width:34px;height:34px;border-radius:50%;background:radial-gradient(circle at 40% 40%,#5bc24a,#1e6fb8);margin:40px auto 0}
.city-box h3{font-size:21px;font-weight:500;margin-top:20px;letter-spacing:.5px}
.city-tags{display:flex;justify-content:center;gap:33px;font-size:13.5px;font-weight:300;margin-top:30px}
.chips{display:flex;flex-wrap:wrap;justify-content:center;gap:14px 12px;width:680px;margin:30px auto 0}
.chip{height:33px;border-radius:17px;border:1px solid #3a4434;background:#151815;padding:0 16px;display:flex;align-items:center;gap:8px;font-size:12.5px;color:var(--green-bright)}
.chip b{font-weight:400;font-size:9.5px;color:var(--muted)}
.chip.soon{color:#9aa096}

/* cta */
.cta{top:2990px;height:395px;background:linear-gradient(180deg,#8cbf2a,#6cc21d 55%,#3a9a12);text-align:center;color:#0c1a05}
.cta h2{font-size:38px;font-weight:500;margin-top:52px}
.cta p{font-size:15px;line-height:26px;width:780px;margin:12px auto 0;color:var(--cta-text)}
.cta p + p{margin-top:26px}
.cta .btn{margin-top:26px;width:150px;height:45px;background:var(--lime);color:#0b1a05}

/* footer */
.footer{top:3385px;height:403px;background:radial-gradient(ellipse 260px 200px at 160px 280px,rgba(140,220,40,.7),transparent 70%),var(--bg)}
.footer .brand{position:absolute;left:111px;top:68px;font-size:40px}
.footer .brand-dot{width:76px;height:76px}
.f-col{position:absolute;top:62px}
.f-col h4{font-size:20px;font-weight:600;margin-bottom:14px}
.f-col a{display:flex;align-items:center;gap:10px;font-size:15px;line-height:34px}
.f-col a svg{width:12px;height:12px;fill:var(--white)}
.contact-item{display:flex;align-items:center;gap:14px;font-size:15px;line-height:26px;margin-bottom:16px}
.contact-item i{width:30px;height:30px;border-radius:50%;background:var(--white);display:flex;align-items:center;justify-content:center;flex:none}
.contact-item svg{width:16px;height:16px;fill:#111}
.f-rule{position:absolute;left:111px;right:112px;top:313px;height:1px;background:#5a5e57}
.copy{position:absolute;top:352px;left:0;right:0;text-align:center;font-size:15px;font-weight:500}
</style>
</head>
<body>
<div class="page">

<header class="section hero">
  <nav class="nav">
    <a class="brand" href="#"><span class="brand-dot"></span>Rallyvo</a>
    <div class="nav-links">
      <a class="active" href="#">Home</a><span>|</span>
      <a href="#">How it Works</a><span>|</span>
      <a href="#">Clubs</a><span>|</span>
      <a href="#">Events</a>
    </div>
    <a class="login" href="#">Login <i></i></a>
  </nav>
  <div class="nav-rule"></div>
  <div class="hero-copy">
    <div class="hero-label">Rallyvo</div>
    <h1 class="hero-title">Play More.<br>Connect Faster.<br><span class="accent">Complete Anywhere.</span></h1>
    <p class="hero-text">Find matches, join games, and connect with players and clubs near you — all in one platform.</p>
    <div class="hero-actions">
      <a class="btn btn-lime" href="#">Get Started</a>
      <a class="btn btn-deep" href="#">Explore Matches</a>
    </div>
  </div>
  <div class="app-preview" role="img" aria-label="Mobile app screens showing Play Now and Find Matches"></div>
</header>

<section class="section stats">
  <div class="stat"><svg viewBox="0 0 48 48"><circle cx="26" cy="8" r="4"/><path d="M24 14l-6 12 8 6-4 12M20 22l-8 2M26 32l10 4"/><circle cx="14" cy="40" r="4"/></svg><div class="stat-num">50K+</div><div class="stat-label">Registered Players</div></div>
  <div class="stat"><svg viewBox="0 0 48 48"><path d="M10 8h28v20c0 8-7 13-14 16-7-3-14-8-14-16z"/><circle cx="24" cy="24" r="7"/></svg><div class="stat-num">1K+</div><div class="stat-label">Clubs &amp; Venues</div></div>
  <div class="stat"><svg viewBox="0 0 48 48"><circle cx="24" cy="26" r="16"/><path d="M8 26h32M24 10c-6 8-6 24 0 32M24 10c6 8 6 24 0 32"/></svg><div class="stat-num">12+</div><div class="stat-label">Countries</div></div>
  <div class="stat"><svg viewBox="0 0 48 48"><circle cx="24" cy="24" r="16"/><path d="M24 8v32M8 24h32M12 13c8 6 16 6 24 0M12 35c8-6 16-6 24 0"/></svg><div class="stat-num">95K+</div><div class="stat-label">Matches Played</div></div>
</section>

<section class="section audiences">
  <h2 class="sec-title">Built For How People<br><span class="accent">Actually Play Sports</span></h2>
  <p class="sec-sub">Whether you're a casual player, a club owner, or an event organizer — Rallyvo has you covered.</p>
  <div class="cards">
    <article class="card">
      <div class="card-icon"><svg viewBox="0 0 40 40"><circle cx="20" cy="7" r="3.5"/><path d="M20 12v12l-5 10M20 24l5 10M14 18h12"/></svg></div>
      <h3>FOR PLAYERS</h3>
      <p>Find games instantly, meet players at your level, and never miss a match again.</p>
      <ul>
        <li><svg viewBox="0 0 14 14"><path d="M2 7l3 3 7-7"/></svg>Smart skill-based matchmaking</li>
        <li><svg viewBox="0 0 14 14"><path d="M2 7l3 3 7-7"/></svg>Instant or scheduled games</li>
        <li><svg viewBox="0 0 14 14"><path d="M2 7l3 3 7-7"/></svg>Performance &amp; stats dashboard</li>
        <li><svg viewBox="0 0 14 14"><path d="M2 7l3 3 7-7"/></svg>Play in 12+ countries</li>
      </ul>
    </article>
    <article class="card">
      <div class="card-icon"><svg viewBox="0 0 40 40"><path d="M8 6h24v16c0 7-6 11-12 13-6-2-12-6-12-13z"/><circle cx="20" cy="19" r="6"/></svg></div>
      <h3>FOR CLUBS</h3>
      <p>Fill courts, manage players, and grow your community with powerful club tools.</p>
      <ul>
        <li><svg viewBox="0 0 14 14"><path d="M2 7l3 3 7-7"/></svg>Court booking management</li>
        <li><svg viewBox="0 0 14 14"><path d="M2 7l3 3 7-7"/></svg>Member management portal</li>
        <li><svg viewBox="0 0 14 14"><path d="M2 7l3 3 7-7"/></svg>Automatic match filling</li>
        <li><svg viewBox="0 0 14 14"><path d="M2 7l3 3 7-7"/></svg>Revenue &amp; analytics tools</li>
      </ul>
    </article>
    <article class="card">
      <div class="card-icon"><svg viewBox="0 0 40 40"><rect x="6" y="9" width="24" height="22" rx="2"/><path d="M6 15h24M12 6v6M24 6v6"/><circle cx="30" cy="30" r="5"/></svg></div>
      <h3>FOR ORGANIZERS</h3>
      <p>Run events, leagues, and tournaments without the spreadsheet chaos.</p>
      <ul>
        <li><svg viewBox="0 0 14 14"><path d="M2 7l3 3 7-7"/></svg>Tournament bracket management</li>
        <li><svg viewBox="0 0 14 14"><path d="M2 7l3 3 7-7"/></svg>Registration &amp; payment flows</li>
        <li><svg viewBox="0 0 14 14"><path d="M2 7l3 3 7-7"/></svg>Real-time leaderboards</li>
        <li><svg viewBox="0 0 14 14"><path d="M2 7l3 3 7-7"/></svg>Automated notifications</li>
      </ul>
    </article>
  </div>
</section>

<section class="section about">
  <div class="about-media" role="img" aria-label="Player's boot striking a football on a glowing stadium pitch"></div>
  <div class="about-copy">
    <h2>About Rallyvo</h2>
    <p>Rallyvo is a global sports networking platform designed to bring players, clubs, and organizers together in one seamless experience. We make it easy to find matches, join events, and connect with your local sports community — whether you're playing casually or competing at a higher level.</p>
    <p>Starting with Pickleball and Padel, Rallyvo is expanding across sports and cities worldwide, building a connected ecosystem where every game begins with a tap. Our mission is simple: make playing sports easier, smarter, and more connected everywhere. Rallyvo is where sports meet connection. We're building the world's most connected sports network.</p>
    <a class="btn" href="#">Read More</a>
  </div>
</section>

<section class="section cities">
  <h2 class="sec-title">Launching City By <span class="accent">City, Worldwide</span></h2>
  <p class="sec-sub">Building the first truly global sports network — starting with Pickleball &amp; Padel, expanding to all sports.</p>
  <div class="city-box">
    <div class="globe"></div>
    <h3>NOW LIVE IN 28 CITIES</h3>
    <div class="city-tags"><span>Building the first global sports network</span><span>Starting with Pickleball &amp; Padel</span><span>Expanding to all sports</span></div>
    <div class="chips">
      <span class="chip"><b>US</b>Miami</span>
      <span class="chip"><b>US</b>New York</span>
      <span class="chip"><b>ES</b>Barcelona</span>
      <span class="chip"><b>FR</b>Paris</span>
      <span class="chip"><b>GB</b>London</span>
      <span class="chip"><b>IT</b>Milan</span>
      <span class="chip"><b>NL</b>Amsterdam</span>
      <span class="chip"><b>DE</b>Berlin</span>
      <span class="chip soon"><b>JP</b>Tokyo - coming soon</span>
      <span class="chip soon"><b>IN</b>Mumbai - coming soon</span>
      <span class="chip soon"><b>BR</b>Sao Paulo - coming soon</span>
      <span class="chip soon"><b>AU</b>Sydney - coming soon</span>
    </div>
  </div>
</section>

<section class="section cta">
  <h2>Ready To Find Your Next Game?</h2>
  <p>Join a growing global network of players, clubs, and organizers — expanding city by city. From finding matches to managing games and events, Rallyvo simplifies your entire sports experience. No more searching. Discover games, connect with players, and start playing in seconds.</p>
  <p>Whether you're a casual player or a competitive club, Rallyvo brings everyone together. We're building the future of sports networking, one community at a time.</p>
  <a class="btn" href="#">Start Playing</a>
</section>

<footer class="section footer">
  <a class="brand" href="#"><span class="brand-dot"></span>Rallyvo</a>
  <div class="f-col" style="left:455px">
    <h4>Quick Links</h4>
    <a href="#"><svg viewBox="0 0 12 12"><path d="M0 5h7V1l5 5-5 5V7H0z"/></svg>Home</a>
    <a href="#"><svg viewBox="0 0 12 12"><path d="M0 5h7V1l5 5-5 5V7H0z"/></svg>About</a>
    <a href="#"><svg viewBox="0 0 12 12"><path d="M0 5h7V1l5 5-5 5V7H0z"/></svg>How It Works</a>
    <a href="#"><svg viewBox="0 0 12 12"><path d="M0 5h7V1l5 5-5 5V7H0z"/></svg>Clubs</a>
    <a href="#"><svg viewBox="0 0 12 12"><path d="M0 5h7V1l5 5-5 5V7H0z"/></svg>Events</a>
  </div>
  <div class="f-col" style="left:678px">
    <h4>Help Links</h4>
    <a href="#"><svg viewBox="0 0 12 12"><path d="M0 5h7V1l5 5-5 5V7H0z"/></svg>FAQ</a>
    <a href="#"><svg viewBox="0 0 12 12"><path d="M0 5h7V1l5 5-5 5V7H0z"/></svg>Terms of use</a>
    <a href="#"><svg viewBox="0 0 12 12"><path d="M0 5h7V1l5 5-5 5V7H0z"/></svg>Privacy Policy</a>
    <a href="#"><svg viewBox="0 0 12 12"><path d="M0 5h7V1l5 5-5 5V7H0z"/></svg>Support Links</a>
    <a href="#"><svg viewBox="0 0 12 12"><path d="M0 5h7V1l5 5-5 5V7H0z"/></svg>Contact Us</a>
  </div>
  <div class="f-col" style="left:897px">
    <h4>Contact Us</h4>
    <div class="contact-item"><i><svg viewBox="0 0 16 16"><path d="M8 1a5 5 0 0 0-5 5c0 4 5 9 5 9s5-5 5-9a5 5 0 0 0-5-5zm0 7a2 2 0 1 1 0-4 2 2 0 0 1 0 4z"/></svg></i><span>Rallyvo<br>United States</span></div>
    <div class="contact-item"><i><svg viewBox="0 0 16 16"><path d="M4 1l3 3-2 2c1 2 3 4 5 5l2-2 3 3-2 3C7 14 2 9 1 3z"/></svg></i><span>+1 555 010 2040</span></div>
    <div class="contact-item"><i><svg viewBox="0 0 16 16"><path d="M1 3h14v10H1zm1 1l6 5 6-5"/></svg></i><span>info@rallyvo.net</span></div>
  </div>
  <div class="f-rule"></div>
  <div class="copy">Copyrights@2026.Rallyvo.All Rights Reserved</div>
</footer>

</div>
</body>
</html>
```